Home Remodeling company needs a business card design

we need a business card design for home remodeling company in hamilton county, indiana USA. we offers a wide range of construction services including whole house renovations, Design and Build Basements and Kitchen and Bathroom Remodeling . we would like to see designs for both site of business card that use the same color of the company logo and also including all information below :
1- Samir Daoudi CEO / General Contractor
2- all company contacts Telephone numbers ( 1-888-TOVAL-42 ) ( 317-555-0192) email address ( info@tovalhome.example) website ( www.tovalhome.example ) and social media logos (Facebook- twitter- google plus )
3- company logo
4- licensed . insured . bonded

```html
<!DOCTYPE html>
<html lang="en">
<head>
<meta charset="utf-8">
<title>Toval Home Remodeling – Business Card</title>
<link rel="stylesheet" href="https://fonts.googleapis.com/css2?family=Lato:wght@400;700&display=swap">
<style>
  :root {
    --brand-red: #c8333f;
    --brand-red-light: #d8454f;
    --brand-red-dark: #b52a36;
    --ink: #333336;
    --ink-soft: #4a4a4e;
    --paper: #ffffff;
    --backdrop: #ecebe8;
  }
  * { margin: 0; padding: 0; box-sizing: border-box; }
  html, body { width: 1200px; height: 950px; overflow: hidden; }
  body {
    background: var(--backdrop);
    font-family: "Lato", "Helvetica Neue", Arial, sans-serif;
    position: relative;
  }
  .card {
    position: absolute;
    width: 760px;
    height: 434px;
    border-radius: 4px;
    box-shadow: 0 10px 30px rgba(0,0,0,0.18);
    overflow: hidden;
  }

  /* Front: red side */
  .card-front {
    left: 90px;
    top: 38px;
    background: linear-gradient(135deg, var(--brand-red-light) 0%, var(--brand-red) 55%, var(--brand-red-dark) 100%);
    color: var(--paper);
    text-align: center;
  }
  .front-mark {
    position: absolute;
    left: 0; right: 0; top: 120px;
    display: flex; align-items: center; justify-content: center; gap: 16px;
  }
  .front-mark .mark-square {
    width: 34px; height: 34px; background: var(--paper);
  }
  .front-mark .mark-name {
    font-weight: 700; font-size: 58px; letter-spacing: 6px; line-height: 1;
  }
  .credentials {
    position: absolute; left: 0; right: 0; top: 262px;
    font-size: 21px; letter-spacing: 1.5px; font-weight: 400;
  }
  .credentials-rule {
    position: absolute; left: 170px; right: 170px; top: 306px; height: 1px;
    background: linear-gradient(90deg, rgba(255,255,255,0), rgba(255,255,255,0.85) 35%, rgba(255,255,255,0.85) 65%, rgba(255,255,255,0));
  }
  .social-dots {
    position: absolute; left: 0; right: 0; top: 296px;
    display: flex; justify-content: center; gap: 8px;
  }
  .social-dots span {
    width: 20px; height: 20px; border-radius: 50%; background: var(--paper);
    border: 2px solid var(--brand-red);
  }

  /* Back: white side */
  .card-back {
    left: 350px;
    top: 490px;
    background: var(--paper);
    color: var(--ink);
  }
  .accent-bar {
    position: absolute; left: 0; top: 150px; width: 9px; height: 190px;
    background: var(--brand-red);
  }
  .contact-block { position: absolute; left: 60px; top: 150px; }
  .person-name { font-weight: 700; font-size: 28px; color: var(--ink); }
  .person-title { font-size: 20px; color: var(--brand-red); margin-top: 2px; margin-bottom: 14px; }
  .contact-list { list-style: none; }
  .contact-list li {
    display: flex; align-items: center; gap: 12px;
    font-size: 18px; color: var(--ink-soft); line-height: 28px;
  }
  .contact-list svg { width: 16px; height: 16px; fill: var(--ink); flex: none; }

  .company-name {
    position: absolute; right: 60px; top: 232px;
    font-weight: 700; font-size: 26px; line-height: 1.2; letter-spacing: 1px;
    color: var(--ink); white-space: nowrap;
  }
</style>
</head>
<body>

  <section class="card card-front" aria-label="Card front">
    <div class="front-mark">
      <span class="mark-square"></span>
      <span class="mark-name">TOVAL</span>
    </div>
    <p class="credentials">LICENSED | INSURED | BONDED</p>
    <div class="credentials-rule"></div>
    <div class="social-dots" aria-label="Social media links">
      <span></span><span></span><span></span>
    </div>
  </section>

  <section class="card card-back" aria-label="Card back">
    <div class="accent-bar"></div>
    <div class="contact-block">
      <h1 class="person-name">Samir Daoudi</h1>
      <p class="person-title">CEO / General Contractor</p>
      <ul class="contact-list">
        <li>
          <svg viewBox="0 0 16 16"><path d="M3.5 1 L6 1 L7 4.5 L5.3 5.8 C6.2 7.8 8.2 9.8 10.2 10.7 L11.5 9 L15 10 L15 12.5 C15 13.9 13.9 15 12.5 15 C6.7 15 1 9.3 1 3.5 C1 2.1 2.1 1 3.5 1 Z"/></svg>
          1-888-TOVAL-42
        </li>
        <li>
          <svg viewBox="0 0 16 16"><path d="M4 0 H12 A1.5 1.5 0 0 1 13.5 1.5 V14.5 A1.5 1.5 0 0 1 12 16 H4 A1.5 1.5 0 0 1 2.5 14.5 V1.5 A1.5 1.5 0 0 1 4 0 Z M4.5 2 V12 H11.5 V2 Z M8 13 A1 1 0 1 0 8 15 A1 1 0 1 0 8 13 Z"/></svg>
          317-555-0192
        </li>
        <li>
          <svg viewBox="0 0 16 16"><path d="M1 3 H15 V4 L8 9 L1 4 Z M1 5.5 L8 10.5 L15 5.5 V13 H1 Z"/></svg>
          info@tovalhome.example
        </li>
        <li>
          <svg viewBox="0 0 16 16"><path d="M8 0.5 A7.5 7.5 0 1 0 8 15.5 A7.5 7.5 0 1 0 8 0.5 Z M5 4 L8 5 L7 8 L9.5 9.5 L8.5 13 L6 11 L6.5 8.5 L4 7 Z M10 2.5 L12.5 4 L11 6 Z"/></svg>
          www.tovalhome.example
        </li>
      </ul>
    </div>
    <p class="company-name">Toval Home Remodeling</p>
  </section>

</body>
</html>
```